Coral Bay Dental Surgery Business Cards

Hi there

Can i please have a simple business card designed (front and back with a black background) using out white reverse logo and the same font used for the logo?
On the back we can just have the logo. Full details at the front part.
Here are the details:

Name of the surgery: Coral Bay | Dental Surgery
Name on the business card: Dr Owen Thackery
Credentials:
BDSc (KTL)
MSc Oral Implantology (Halvorsen, Frankfurt)
Fellow & Diplomate (Meridian Council of Restorative Prosthetics)

Email: owen.thackery@coralbaysmile.example
Address: 17 Lisgrove Rd Karrinyup
Website: coralbaysmile.example
Phone: 1800 316 482

We have attached our high res logo and a rudimentary version of the business card which is not necessarily what we want but gives all the details
We would like to have the print ready version. Thanks.

Contact Information for Business Card

website. credentials. qr code. address. phone number

Requirements
Must have
• QR code

```html
<!DOCTYPE html>
<html lang="en">
<head>
<meta charset="utf-8">
<title>Coral Bay Dental Surgery – Business Cards</title>
<link rel="stylesheet" href="https://fonts.googleapis.com/css2?family=Montserrat:wght@600;700&family=Open+Sans:wght@400;600&display=swap">
<style>
  :root {
    --paper: #e6e6e4;
    --card: #1f1f1f;
    --teal: #1ec8c0;
    --blue: #1a95b8;
    --white: #ffffff;
    --muted: #e8e8e8;
    --qr-light: #f2f2f2;
  }
  * { box-sizing: border-box; margin: 0; padding: 0; }
  html, body { width: 1200px; height: 801px; overflow: hidden; }
  body {
    background: var(--paper);
    font-family: "Open Sans", Arial, sans-serif;
    display: flex;
    align-items: center;
    justify-content: center;
    gap: 40px;
  }
  .card {
    position: relative;
    width: 560px;
    height: 320px;
    background: var(--card);
    border-bottom: 4px solid var(--teal);
    box-shadow: 0 10px 24px rgba(0,0,0,0.22);
    color: var(--white);
  }

  /* Front */
  .brand {
    position: absolute;
    top: 38px;
    right: 36px;
    display: flex;
    align-items: center;
    gap: 10px;
    font-family: "Montserrat", Arial, sans-serif;
    font-weight: 600;
    font-size: 17px;
    letter-spacing: 0.04em;
    color: var(--white);
  }
  .brand-dot {
    width: 14px; height: 14px;
    border-radius: 50%;
    background: var(--blue);
    flex: none;
  }
  .holder { position: absolute; left: 36px; top: 118px; right: 36px; }
  .holder-name {
    font-family: "Montserrat", Arial, sans-serif;
    font-weight: 700;
    font-size: 24px;
    color: var(--teal);
    line-height: 1.1;
  }
  .credentials { margin-top: 8px; font-size: 11px; line-height: 1.5; color: var(--muted); }
  .divider {
    position: absolute;
    left: 36px; right: 36px; top: 214px;
    height: 1px;
    background: var(--teal);
  }
  .contacts {
    position: absolute;
    left: 36px; top: 230px;
    list-style: none;
    font-size: 12px;
    line-height: 1.75;
    color: var(--muted);
  }
  .contacts li { display: flex; align-items: center; gap: 8px; }
  .contacts svg { width: 12px; height: 12px; fill: var(--teal); flex: none; }
  .contacts .accent { color: var(--teal); }
  .address {
    position: absolute;
    right: 112px; top: 236px;
    text-align: right;
    font-size: 12px;
    line-height: 1.5;
    color: var(--muted);
  }
  .qr-code {
    position: absolute;
    right: 36px; top: 228px;
    width: 64px; height: 64px;
    background: var(--qr-light);
    border: 4px solid var(--qr-light);
  }

  /* Back */
  .back-brand {
    position: absolute;
    right: 40px;
    bottom: 70px;
    display: flex;
    align-items: center;
    gap: 12px;
    font-family: "Montserrat", Arial, sans-serif;
    font-weight: 600;
    font-size: 26px;
    letter-spacing: 0.04em;
    color: var(--white);
  }
  .back-brand .brand-dot { width: 20px; height: 20px; }
</style>
</head>
<body>

  <section class="card card-front" aria-label="Business card front">
    <div class="brand"><span class="brand-dot"></span><span>Coral Bay Dental Surgery</span></div>

    <div class="holder">
      <h1 class="holder-name">Dr Owen Thackery</h1>
      <p class="credentials">
        BDSc (KTL) / MSc Oral Implantology (Halvorsen, Frankfurt)<br>
        Fellow &amp; Diplomate (Meridian Council of Restorative Prosthetics)
      </p>
    </div>

    <div class="divider"></div>

    <ul class="contacts">
      <li>
        <svg viewBox="0 0 24 24" aria-hidden="true"><path d="M6.6 10.8a15.1 15.1 0 0 0 6.6 6.6l2.2-2.2a1 1 0 0 1 1-.25 11.4 11.4 0 0 0 3.6.57 1 1 0 0 1 1 1V20a1 1 0 0 1-1 1A17 17 0 0 1 3 4a1 1 0 0 1 1-1h3.5a1 1 0 0 1 1 1c0 1.25.2 2.45.57 3.6a1 1 0 0 1-.25 1z"/></svg>
        <span>1800 316 482</span>
      </li>
      <li>
        <svg viewBox="0 0 24 24" aria-hidden="true"><path d="M2 5h20v14H2zm2 2v.4l8 5 8-5V7zm0 2.8V17h16V9.8l-8 5z"/></svg>
        <span>owen.thackery@coralbaysmile.example</span>
      </li>
      <li>
        <svg viewBox="0 0 24 24" aria-hidden="true"><circle cx="12" cy="12" r="10"/></svg>
        <span>www.<span class="accent">coralbaysmile</span>.example</span>
      </li>
    </ul>

    <p class="address">17 Lisgrove Rd<br>Karrinyup</p>

    <div class="qr-code" role="img" aria-label="QR code linking to the surgery website"></div>
  </section>

  <section class="card card-back" aria-label="Business card back">
    <div class="back-brand"><span class="brand-dot"></span><span>Coral Bay Dental Surgery</span></div>
  </section>

</body>
</html>
```